MOLT - Monitoring Natural Hazards from Space Web Application

KORVEN Sarl is a Luxembourg based Space-Startup that works in the field of Earth Observation. KORVEN is a platform able to extract value-added information from satellite data and is specialized in mapping Natural Disaster (floods, fires etc).

We are now developing a new vertical tool, called MOLT, dedicated to the monitoring of natural hazards in Humanitarian Camps around the world.

The goal of MOLT is to hide to the users' all the complexity of the Satellite Image processing and just provide them the results.

This project require to Design 4 pages of MOLT:
• Public Home Page (Code - V01)
• Dashboard (private Home Page) (Code - V03)
• Monitor (web GIS) (Code - V14)
• Registration Page (Code - V04)

We would like to provide the required time to make a good job.

Target Market(s)

Humanitarian Agencies, Goverments

Coding

Coded - Design and coding required

Number of Pages Required

4 page

Font styles to use
Other font styles liked:
• see the manual attached

Requirements
Must have
• 4 pages. One Home, one form, one dashboard and one web map.
Nice to have
• Please read the attachment with all the detailed instructions

```html
<!DOCTYPE html>
<html lang="en">
<head>
<meta charset="utf-8">
<title>Register in MOLT</title>
<link href="https://fonts.googleapis.com/css2?family=Jost:wght@400;500&family=Space+Mono:wght@700&display=swap" rel="stylesheet">
<style>
:root{
  --teal:#274d5a;
  --teal-dark:#234957;
  --ink:#1d3a45;
  --gold:#edb942;
  --field:#f2f4f6;
  --field-line:#c9ced3;
  --muted:#9aa1a6;
  --white:#ffffff;
}
*{box-sizing:border-box;margin:0;padding:0}
html,body{width:951px;height:1200px;overflow:hidden;background:var(--white)}
body{position:relative;font-family:'Jost',sans-serif;color:var(--ink)}
.abs{position:absolute}
/* header */
.site-header{position:absolute;left:0;top:0;width:951px;height:72px;background:var(--teal)}
.brand{position:absolute;display:flex;align-items:center;gap:19px}
.brand-dot{width:47px;height:47px;border:2px solid var(--gold);border-radius:50%}
.brand-name{font-family:'Jost',sans-serif;font-weight:400;color:var(--white);font-size:34px;letter-spacing:6px}
.nav-link{position:absolute;top:28px;color:var(--white);font-size:13px;font-weight:500;transform:translateX(-50%)}
.btn-outline,.btn-gold{position:absolute;top:22px;height:31px;width:93px;border-radius:16px;display:flex;align-items:center;justify-content:center;font-size:11.5px;font-weight:500;color:var(--white)}
.btn-outline{left:695px;border:1px solid var(--white)}
.btn-gold{left:797px;background:var(--gold)}
/* title */
.page-title{position:absolute;left:0;width:951px;top:123px;text-align:center;font-family:'Space Mono',monospace;font-weight:700;font-size:30px;letter-spacing:1px;color:var(--ink)}
.title-rule{position:absolute;left:438px;top:170px;width:58px;height:2px;background:var(--gold)}
/* form card */
.card{position:absolute;left:89px;top:194px;width:782px;height:620px;background:var(--white);border:1px solid #b7bdc1}
.label{position:absolute;font-size:13.5px;color:var(--ink)}
.field{position:absolute;height:43px;background:var(--field);border:1px solid var(--field-line);font-size:12px;color:#6f777c;display:flex;align-items:center;padding-left:14px}
.field.big{font-size:14px;color:var(--muted);padding-left:16px}
.hint{position:absolute;font-size:9.8px;line-height:13.5px;color:var(--ink)}
.check{position:absolute;left:132px;width:19px;height:17px;background:var(--field);border:1px solid var(--field-line)}
.check-text{position:absolute;left:161px;font-size:11px;color:var(--ink)}
.submit{position:absolute;left:131px;top:749px;width:128px;height:38px;border-radius:19px;background:var(--gold);color:var(--white);font-size:13px;font-weight:500;display:flex;align-items:center;justify-content:center}
.chev{position:absolute;right:12px;top:15px}
/* footer */
.site-footer{position:absolute;left:0;top:857px;width:951px;height:276px;background:var(--teal)}
.footer-base{position:absolute;left:0;top:1133px;width:951px;height:67px;background:var(--teal-dark)}
.social{position:absolute;top:992px;width:28px;height:28px;border:1.3px solid var(--white);border-radius:50%}
.foot-title{position:absolute;top:924px;font-size:20px;color:var(--white)}
.foot-rule{position:absolute;top:952px;width:32px;height:1.5px;background:var(--gold)}
.foot-link{position:absolute;left:401px;font-size:13px;color:var(--white)}
.contact-text{position:absolute;left:664px;font-size:13px;line-height:16.5px;color:var(--white)}
.copyright{position:absolute;left:0;width:972px;top:1149px;text-align:center;font-size:11.5px;color:#b7c4c9}
</style>
</head>
<body>

<header class="site-header">
  <div class="brand" style="left:74px;top:16px"><span class="brand-dot"></span><span class="brand-name">MOLT</span></div>
  <span class="nav-link" style="left:425px">HOME</span>
  <span class="nav-link" style="left:526px">FEATURES</span>
  <span class="nav-link" style="left:633px">PRICING</span>
  <span class="btn-outline">REGISTER</span>
  <span class="btn-gold">LOGIN</span>
</header>

<svg class="abs" style="left:454px;top:100px" width="26" height="26" viewBox="0 0 26 26"><path d="M13 0 Q14 12 26 13 Q14 14 13 26 Q12 14 0 13 Q12 12 13 0Z" fill="var(--gold)"/></svg>
<h1 class="page-title">REGISTER IN MOLT</h1>
<div class="title-rule"></div>

<svg class="abs" style="left:0;top:0" width="951" height="830"><polygon points="78,628 89,625 871,491 882,487 882,824 78,824" fill="var(--gold)"/></svg>
<div class="card"></div>

<!-- left column -->
<span class="label" style="left:138px;top:227px">User Id</span>
<div class="field" style="left:134px;top:252px;width:317px"></div>
<span class="hint" style="left:141px;top:301px">UserId of at least 8 characters</span>

<span class="label" style="left:136px;top:331px">Password</span>
<div class="field" style="left:134px;top:354px;width:317px"></div>
<span class="hint" style="left:133px;top:404px;width:320px">Password of at least 8 characters that mix at least one char, one number and one special symbol.</span>

<span class="label" style="left:134px;top:447px">Confirm Password</span>
<div class="field" style="left:133px;top:470px;width:317px"></div>

<span class="label" style="left:132px;top:525px">Name</span>
<div class="field" style="left:130px;top:548px;width:151px"></div>
<span class="label" style="left:297px;top:525px">Surname</span>
<div class="field" style="left:296px;top:548px;width:151px"></div>

<span class="label" style="left:131px;top:601px">Mobile Number</span>
<div class="field" style="left:130px;top:623px;width:317px"></div>

<span class="check" style="top:691px"></span>
<span class="check-text" style="top:691px">I have read and Accept the MOLT Terms and Conditions</span>
<span class="check" style="top:713px"></span>
<span class="check-text" style="top:714px">I have read and Accept the MOLT Privacy Policy</span>

<span class="submit">REGISTER</span>

<!-- right column -->
<span class="label" style="left:509px;top:229px">E-mail</span>
<div class="field" style="left:508px;top:251px;width:317px"></div>

<span class="label" style="left:506px;top:330px">Confirm E-mail</span>
<div class="field" style="left:505px;top:353px;width:317px"></div>

<span class="label" style="left:507px;top:404px">Organization Name</span>
<div class="field" style="left:507px;top:426px;width:317px">Humanitarian NGO</div>

<span class="label" style="left:507px;top:483px">Organization Type</span>
<div class="field" style="left:507px;top:505px;width:317px">Select
  <svg class="chev" width="14" height="10" viewBox="0 0 14 10"><path d="M1 2 L7 8 L13 2" fill="none" stroke="#5b6469" stroke-width="1.8"/></svg></div>

<span class="label" style="left:507px;top:561px">Organization Address</span>
<div class="field big" style="left:507px;top:583px;width:153px">City</div>
<div class="field big" style="left:668px;top:583px;width:153px">Street</div>
<div class="field big" style="left:506px;top:638px;width:153px">Number</div>
<div class="field big" style="left:667px;top:638px;width:153px">Postal Code</div>
<div class="field big" style="left:506px;top:692px;width:153px">Telephone</div>
<div class="field big" style="left:668px;top:692px;width:153px">Country
  <svg class="chev" width="14" height="10" viewBox="0 0 14 10"><path d="M1 2 L7 8 L13 2" fill="none" stroke="#5b6469" stroke-width="1.8"/></svg></div>

<!-- footer -->
<footer class="site-footer"></footer>
<div class="brand" style="left:115px;top:926px"><span class="brand-dot"></span><span class="brand-name">MOLT</span></div>
<span class="social" style="left:124px"></span>
<span class="social" style="left:163px"></span>
<span class="social" style="left:201px"></span>
<span class="social" style="left:236px"></span>
<span class="social" style="left:273px"></span>

<span class="foot-title" style="left:398px">Quick Links</span>
<span class="foot-rule" style="left:399px"></span>
<span class="foot-link" style="top:966px">Features</span>
<span class="foot-link" style="top:989px">Pricing</span>
<span class="foot-link" style="top:1012px">Register</span>
<span class="foot-link" style="top:1035px">Login</span>

<span class="foot-title" style="left:622px">Contact Us</span>
<span class="foot-rule" style="left:623px"></span>
<svg class="abs" style="left:623px;top:970px" width="26" height="26" viewBox="0 0 26 26" fill="none" stroke="var(--white)" stroke-width="1.3"><path d="M5 3 L9 3 L11 8 L8 10 Q10 15 15 18 L17 15 L22 17 L22 21 Q20 24 16 22 Q7 18 3 8 Q2 4 5 3Z"/><path d="M15 5 Q20 6 21 11"/><path d="M15 1 Q24 2 25 11"/></svg>
<span class="contact-text" style="top:966px">Phone Number<br>(555) 014-3390</span>
<svg class="abs" style="left:625px;top:1022px" width="25" height="20" viewBox="0 0 25 20" fill="none" stroke="var(--white)" stroke-width="1.4"><rect x="1" y="1" width="23" height="18"/><path d="M1 1 L12.5 11 L24 1"/></svg>
<span class="contact-text" style="top:1017px">Email address<br>hello@moltplatform.org</span>

<div class="footer-base"></div>
<p class="copyright">© 2024 Company Name | All Rights Reserved</p>

</body>
</html>
```